Redesign of Banner & Navigation

We are rebranding our internal application and need to have the top section redesigned (navigation and above). A successful design will lead to further projects reworking actual content.

Fortunately, design in our industry is pretty bad, so coming up with something compelling that integrates our new logo shouldn't be a monumental effort.  Basically, I am looking for a "fresh look" that either incorporates or complements the new logos colors (which I have no control over).

http://www.veloquin.com/products.aspx?featureID=2&typeID=1http://www.veloquin.com/products.aspx?featureID=2&typeID=1http://www.veloquin.com/products.aspx?featureID=2&typeID=1

Examples of similar systems:

Veloquin Grid

http://www.veloquin.com/products.aspx?featureID=2&typeID=1

BrimPath QVE

http://www.brimpath.com/products/qvechange.aspx#container-DemosandResources

dunvoQHR Net

http://www.dunvoqhr.com/products/dunvoqhrnet/

WDT Keystel

http://www.wdtfil.com/pages/keystel

Oskelund QHR

http://www.oskelund.com/prod/qhr/VBE_May_2011_Flyer.pdf

 

Target Market(s)

30,000 Real Estate professionals.

Requirements
Must have
• Clean, highly-usable design.
Nice to have
• Minimal bandwidth overhead.
Should not have
• Flash, animation, non-image (JPG/GIF/PNG) elements.

```html
<!DOCTYPE html>
<html lang="en">
<head>
<meta charset="utf-8">
<title>Kestrion — Home</title>
<link rel="stylesheet" href="https://fonts.googleapis.com/css2?family=Didact+Gothic&family=Noto+Sans:wght@400;700&display=swap">
<style>
:root{
  --bg-band:#e8e0d1;
  --bg-band-light:#f3efe7;
  --top-bar:#3a1e1c;
  --orange:#f7941e;
  --orange-light:#fbb44a;
  --ink:#222;
  --muted:#888;
  --link:#1a7fc1;
  --red:#e0261b;
  --box-head:#f3efe4;
  --box-border:#ddd3b8;
  --row:#f8f6ee;
  --panel:#fff;
  --qs-bg:#ebe3cf;
  --gray-head:#6b6b6b;
}
*{box-sizing:border-box;margin:0;padding:0}
html,body{width:1200px;height:1031px;overflow:hidden}
body{font-family:"Noto Sans",Verdana,sans-serif;font-size:11px;color:var(--ink);
  background:linear-gradient(to bottom,var(--bg-band-light) 0,var(--bg-band) 363px,#fff 363px);position:relative}
a{color:var(--link);text-decoration:none}
.top-bar{height:9px;background:linear-gradient(to bottom,#1e0d0c,var(--top-bar))}
.head{font-family:"Didact Gothic",sans-serif}
.brand{position:absolute;left:141px;top:24px;display:flex;align-items:center;gap:10px}
.brand-dot{width:22px;height:22px;border-radius:50%;background:var(--orange)}
.brand-name{font-family:"Didact Gothic",sans-serif;font-size:44px;color:var(--ink);letter-spacing:-1px}
.util{position:absolute;right:143px;display:flex;font-size:10.5px}
.util a{color:var(--ink);padding:0 9px;border-left:1px solid #ccc}
.util a:first-child{border-left:0}
.util .new{color:var(--orange)}
.util-top{top:32px}
.util-second{top:80px;align-items:center}
.sign-in{background:var(--orange);color:#fff!important;border-radius:2px;padding:2px 6px!important;margin-left:6px;border:0!important;font-size:12px}
.rule{position:absolute;left:141px;width:918px;top:108px;border-top:1px dotted #c8bda4}
.nav{position:absolute;left:141px;top:120px;display:flex;gap:10px;font-family:"Didact Gothic",sans-serif;font-size:19px}
.nav a{color:#444;padding:3px 10px}
.nav .active{background:var(--orange);color:#fff;border-radius:3px;border:1px solid #e07c10}
.qs-title{position:absolute;left:839px;top:130px;font-family:"Didact Gothic",sans-serif;font-size:18px;color:#555}
.qs-icon{position:absolute;left:1003px;top:121px}
.panel{position:absolute;left:141px;top:165px;width:918px;height:825px;background:var(--panel);box-shadow:0 0 3px rgba(0,0,0,.08)}
.col-left{position:absolute;left:9px;top:9px;width:211px}
.box{border:1px solid var(--box-border);margin-bottom:19px;background:var(--row)}
.box-title{font-family:"Didact Gothic",sans-serif;font-size:17px;padding:6px 8px;background:var(--box-head);border-bottom:1px solid var(--box-border)}
.box-row{padding:6px 8px;display:flex;align-items:center;gap:8px;font-size:10.5px;background:#efeadc}
.box-note{padding:5px 8px;text-align:center;font-size:10.5px;background:#fffdf4}
.select{border:1px solid #ccc;background:#f7f7f7;color:#777;font-size:10.5px;height:22px;display:flex;align-items:center;justify-content:space-between;padding-left:9px;border-radius:2px}
.select::after{content:"";border-left:1px solid #ccc;width:19px;height:100%;background:linear-gradient(#ccc,#ccc) no-repeat;background:none;display:block;position:relative}
.caret{width:20px;height:100%;border-left:1px solid #ddd;display:flex;align-items:center;justify-content:center}
.caret::before{content:"";border:4px solid transparent;border-top-color:#999;margin-top:4px}
.select::after{display:none}
.hs-item{padding:5px 8px;font-size:10.5px;border-bottom:1px dotted #d4caa9;background:#fffdf4}
.hs-create{text-align:center;color:var(--red);padding:4px;font-size:10.5px;background:#fffdf4}
.alliance{border:1px solid #e2e2e2;background:#fafafa}
.alliance .box-title{background:var(--gray-head);color:#fff;border:0}
.alliance p{padding:6px 8px;font-size:11.5px;color:var(--muted);line-height:19px}
.col-main{position:absolute;left:239px;top:17px;width:440px}
.section-title{font-family:"Didact Gothic",sans-serif;font-size:19px;padding-bottom:10px;border-bottom:3px solid #ddd;margin-bottom:14px}
.post{margin-bottom:15px;font-size:11.6px;line-height:18.8px}
.post time{color:#555;font-size:11px}
.tag{background:var(--red);color:#fff;font-size:8px;padding:0 3px;margin-right:4px;vertical-align:1px}
.post h3{font-size:11.6px;font-weight:700;color:#555;letter-spacing:.2px}
.post p{color:var(--muted)}
.contact{font-size:11.6px;line-height:18.8px;color:var(--muted)}
.col-right{position:absolute;left:698px;top:12px;width:211px}
.quick-search{background:var(--qs-bg);padding:8px 8px 0;height:230px;position:relative;font-size:10.5px}
.qs-row{display:flex;align-items:center;gap:6px;margin-bottom:8px}
.input{background:#fff;border:1px solid #ccc;height:23px;border-radius:2px}
.search-btn{position:absolute;left:12px;top:186px;width:187px;height:41px;border-radius:4px;background:linear-gradient(var(--orange-light),var(--orange));border:1px solid #e08910;font-family:"Didact Gothic",sans-serif;font-size:19px;color:#c65d00;text-align:center;line-height:40px;letter-spacing:1px}
.ql-title{font-family:"Didact Gothic",sans-serif;font-size:17px;margin:16px 0 6px}
.ql{list-style:none}
.ql li{border:1px solid #e6e6e6;height:37px;margin-bottom:3px;display:flex;align-items:center;padding-left:12px;gap:16px;font-size:13px;background:#fcfcfc;color:#222}
.ql svg{width:22px;height:22px;fill:#bbb;flex:none}
.ql .customize{justify-content:center;padding:0;background:#eaf6fd;color:var(--link);font-size:13px;border:1px solid #e6e6e6}
.footer{position:absolute;right:140px;top:1004px;font-size:11.5px;color:#555}
</style>
</head>
<body>
<div class="top-bar"></div>

<div class="brand"><span class="brand-dot"></span><span class="brand-name">Kestrion</span></div>

<nav class="util util-top">
  <a href="#">HLNPRO.com</a><a href="#">Options</a><a href="#"><span class="new">**New**</span> HLN PRO Messages</a>
</nav>
<nav class="util util-second">
  <a href="#">Contact HLN PRO</a><a href="#">Training Library</a><a href="#">Help</a><a class="sign-in" href="#">Sign In</a>
</nav>
<div class="rule"></div>

<nav class="nav">
  <a class="active" href="#">Home</a><a href="#">Clients</a><a href="#">Listings</a><a href="#">Search</a><a href="#">Tools</a>
</nav>
<div class="qs-title">Quick Search</div>
<svg class="qs-icon" width="56" height="48" viewBox="0 0 56 48"><circle cx="22" cy="20" r="15" fill="none" stroke="#888" stroke-width="6"/><line x1="33" y1="31" x2="48" y2="46" stroke="#888" stroke-width="8" stroke-linecap="round"/></svg>

<main class="panel">
  <aside class="col-left">
    <section class="box">
      <div class="box-title">New Client Matches</div>
      <div class="box-row">For the Previous: <span class="select" style="width:97px">24 hours<span class="caret"></span></span></div>
      <div class="box-note">No New Matches Found</div>
    </section>
    <section class="box">
      <div class="box-title">New Listing Matches</div>
      <div class="box-row">For the Previous: <span class="select" style="width:97px">24 hours<span class="caret"></span></span></div>
      <div class="box-note">No New Matches Found</div>
    </section>
    <section class="box">
      <div class="box-title">Hot Sheet Reports</div>
      <div class="hs-item">Cape - different than Kathy's</div>
      <div class="hs-item">Hotsheet 1</div>
      <div class="hs-create">**Create a New Hot Sheer**</div>
    </section>
    <section class="box">
      <div class="box-title">My Listings Due to Expire</div>
      <div class="box-row">In the Next: <span class="select" style="width:97px">2 Weeks<span class="caret"></span></span></div>
      <div class="box-note">No Listings Found</div>
    </section>
    <section class="box">
      <div class="box-title">New Web Sign-ups</div>
      <div class="box-note">No New Sign-ups</div>
    </section>
    <section class="alliance">
      <div class="box-title">Coastline Alliance</div>
      <p><a href="#">Go to RI, State-Wide</a><br>If you have questions with regard to the QVEchage system, please direct them to <a href="#">Statewise HLN.</a></p>
    </section>
  </aside>

  <section class="col-main">
    <h2 class="section-title">System Updates</h2>
    <article class="post"><time><span class="tag">New</span>8/17/2011</time><h3>Last Chance Update to New Blue Vaultkey Now</h3>
      <p>Lorem ipsum dolor sit amet, consectetur adipisicing elit, sed do eiusmod tempor incididunt ut labore et dolore magna aliqua. Ut enim ad minim veniam, quis nostrud exercitation ullamco laboris nisi ut aliquip ex ea commodo consequat. <a href="#">Duis aute irure dolor</a> in reprehenderit in voluptate velit esse cillum dolore eu fugiat nulla pariatur.</p></article>
    <article class="post"><time><span class="tag">New</span>8/9/2011</time><h3>Like What You See with SkyComp CMA?</h3>
      <p>Lorem ipsum dolor sit amet, consectetur adipisicing elit, sed do eiusmod tempor incididunt ut labore et dolore magna aliqua. Ut enim ad minim veniam, <a href="#">quis nostrud exercitation</a> ullamco laboris nisi ut aliquip ex ea commodo consequat.</p></article>
    <article class="post"><time>8/4/2011</time><h3>Harlow Mutual Short Sale Assistance Desk</h3>
      <p>Lorem ipsum dolor sit amet, consectetur adipisicing elit, sed do eiusmod tempor incididunt ut <a href="#">labore et dolore</a> magna aliqua. Ut enim ad minim veniam, quis nostrud exercitation ullamco laboris nisi ut aliquip ex ea commodo consequat.</p></article>
    <article class="post"><time>8/1/2011</time><h3>Tip of the Month - What's Hot in Your Area!</h3>
      <p>Lorem ipsum dolor sit amet, consectetur adipisicing elit, sed do eiusmod tempor incididunt ut <a href="#">labore et dolore</a> magna aliqua. Ut enim ad minim veniam, quis nostrud exercitation ullamco laboris nisi ut aliquip ex ea commodo consequat.</p></article>
    <article class="post"><time>7/25/2011</time><h3>HLN PRO Fee Increase Effective 4th Quarter</h3>
      <p>Lorem ipsum dolor sit amet, consectetur adipisicing elit, sed do eiusmod tempor incididunt ut labore et dolore magna aliqua. Ut enim ad minim veniam, quis nostrud exercitation ullamco laboris nisi ut aliquip ex ea commodo consequat.</p></article>
    <h2 class="section-title" style="margin-top:8px">For HLN PRO Customers</h2>
    <p class="contact"><a href="#">HLN Property Listing Network, Inc.</a><br>Phone: (555) 014-2290</p>
  </section>

  <aside class="col-right">
    <form class="quick-search">
      <div class="qs-row">MLS #: <span class="input" style="width:83px;margin-left:7px"></span></div>
      <div style="text-align:center;margin:-2px 0 5px">OR</div>
      <div class="qs-row">Street #: <span class="input" style="width:40px"></span> Name: <span class="input" style="width:56px"></span></div>
      <div class="qs-row" style="margin-top:12px"><span class="select" style="width:140px">All of Massachusetts<span class="caret"></span></span><span class="select" style="width:40px;padding-left:6px">MA<span class="caret"></span></span></div>
      <div class="qs-row" style="margin-top:14px">Type: <span class="select" style="width:163px">All Property Types<span class="caret"></span></span></div>
      <div class="search-btn">SEARCH NOW</div>
    </form>
    <h2 class="ql-title">Quick Links</h2>
    <ul class="ql">
      <li><svg viewBox="0 0 24 24"><circle cx="12" cy="7" r="5"/><rect x="4" y="13" width="16" height="10" rx="3"/></svg>Daily Receipt</li>
      <li><svg viewBox="0 0 24 24"><circle cx="6" cy="9" r="3"/><circle cx="12" cy="7" r="3"/><circle cx="18" cy="9" r="3"/><rect x="2" y="13" width="20" height="9" rx="2"/></svg>Agent/Office Rosters</li>
      <li><svg viewBox="0 0 24 24"><rect x="5" y="2" width="14" height="20" fill="none" stroke="#bbb" stroke-width="2"/><rect x="8" y="7" width="8" height="2"/><rect x="8" y="12" width="8" height="2"/></svg>CMA</li>
      <li><svg viewBox="0 0 24 24"><circle cx="10" cy="10" r="6" fill="none" stroke="#bbb" stroke-width="2.5"/><line x1="14" y1="14" x2="21" y2="21" stroke="#bbb" stroke-width="3"/></svg>IDX Search Options</li>
      <li><svg viewBox="0 0 24 24"><path d="M4 12v9h16v-9" fill="none" stroke="#bbb" stroke-width="2"/><path d="M12 3l-5 5h3v8h4V8h3z"/></svg>IDX Downloads</li>
      <li><svg viewBox="0 0 24 24"><rect x="3" y="4" width="3" height="18"/><rect x="8" y="9" width="3" height="13"/><rect x="13" y="13" width="3" height="9"/><rect x="18" y="17" width="3" height="5"/></svg>Market Reports</li>
      <li><svg viewBox="0 0 24 24"><rect x="5" y="6" width="3" height="17"/><rect x="3" y="1" width="7" height="5"/><rect x="16" y="6" width="3" height="17"/><rect x="14" y="1" width="7" height="4"/></svg>Options and Settings</li>
      <li><svg viewBox="0 0 24 24"><path d="M2 12L12 3l10 9h-3v10H5V12z"/></svg>Pocket Real Estate</li>
      <li><svg viewBox="0 0 24 24"><rect x="4" y="6" width="18" height="14" fill="none" stroke="#bbb" stroke-width="2"/><rect x="8" y="11" width="10" height="2"/></svg>VOW Editor</li>
      <li><svg viewBox="0 0 24 24"><path d="M1 13L8 6l7 7h-2v8H3v-8z"/><rect x="16" y="6" width="7" height="15" fill="none" stroke="#bbb" stroke-width="1.5"/></svg>Property History</li>
      <li><svg viewBox="0 0 24 24"><rect x="3" y="2" width="18" height="20" rx="2" fill="none" stroke="#bbb" stroke-width="2"/><rect x="7" y="7" width="10" height="2"/><rect x="7" y="11" width="10" height="2"/><rect x="7" y="15" width="10" height="2"/></svg>My Listings</li>
      <li><svg viewBox="0 0 24 24"><circle cx="5" cy="10" r="3"/><circle cx="12" cy="7" r="3"/><circle cx="19" cy="10" r="3"/><rect x="1" y="14" width="22" height="8" rx="2"/></svg>My Clients</li>
      <li><svg viewBox="0 0 24 24"><line x1="2" y1="12" x2="22" y2="12" stroke="#bbb" stroke-width="2"/><circle cx="4" cy="12" r="3"/><path d="M22 12l-4-3v6z"/><line x1="10" y1="12" x2="14" y2="7" stroke="#bbb" stroke-width="2"/><line x1="12" y1="12" x2="16" y2="17" stroke="#bbb" stroke-width="2"/></svg>PC Connection</li>
      <li class="customize">Customize</li>
    </ul>
  </aside>
</main>

<footer class="footer">© Copyright 2011. Kestrion | All rights reserved.</footer>
</body>
</html>
```